Re-design and craft the perfect CV platform

We are building a CV-based platform designed to connect employees and employers, with a strong focus on individual users. As we're just starting out, we're looking to have our platform and logo redesigned to better reflect our vision
https://app.plovanstaffing.com/
Colors like in the logo attached
#87C032 #6A6E71 #618930 - also you can add more colors if you like.
https://app.plovanstaffing.com/dashboard - This page would be nice if you plan it, like personal Bio dashboard. Attached picture (Dashboard wanted) one idea from how we would like to be, but we are open for new professional ideas/solutions.
https://app.plovanstaffing.com/posts - On this page we want to be showed the jobs posted. Attached one picture about our idea (jobs page wanted)
https://app.plovanstaffing.com/profile - design something nice.
Only Photoshop, Illustrator or Frameboard
Other pictures from the app attached (as looking right now)

Target Market(s)

Job seekers, HR, Recruiters

Industry/Entity Type

HR Tech

Number of Pages Required

5+ page

Colors
00AB8E
00BBA5
67D7C9
C6EFE9
E9F9F6

```html
<!DOCTYPE html>
<html lang="en">
<head>
<meta charset="utf-8">
<title>CV Spire – Profile</title>
<link href="https://fonts.googleapis.com/css2?family=Poppins:wght@300;400;500;600&display=swap" rel="stylesheet">
<style>
:root{
  --green:#84bd32;
  --green-dark:#618930;
  --slate:#6a6e71;
  --ink:#3f4245;
  --muted:#b2b2b2;
  --panel:#f3f3f3;
  --side:#fafafa;
  --topbar:#ececec;
  --footer:#a7a7a7;
  --track:#ffffff;
}
*{margin:0;padding:0;box-sizing:border-box}
html,body{width:1200px;height:662px;overflow:hidden}
body{font-family:'Poppins',sans-serif;color:var(--ink);background:#fff;position:relative}
.abs{position:absolute}
.sidebar{left:0;top:0;width:200px;height:631px;background:var(--side)}
.brand{left:0;top:34px;width:200px;text-align:center;font-size:22px;font-weight:600;color:var(--green);letter-spacing:.5px}
.brand-dot{display:inline-block;width:12px;height:12px;border-radius:50%;background:var(--slate);margin-right:7px;vertical-align:1px}
.card{background:var(--panel);border-radius:6px}
.profile{left:6px;top:100px;width:188px;height:255px;text-align:center}
.avatar{position:absolute;left:27px;top:19px;width:134px;height:134px;border-radius:50%;border:1.5px solid var(--green);padding:4px;background:#fff}
.avatar span{display:block;width:100%;height:100%;border-radius:50%;background:radial-gradient(circle at 50% 40%,#c9b4a4,#6b5447 60%,#e3e3e3)}
.profile .name{position:absolute;left:0;right:0;top:157px;font-size:14.5px;font-weight:500;color:var(--slate)}
.profile .name b{color:var(--green);font-weight:500}
.profile .role{position:absolute;left:0;right:0;top:177px;font-size:9.5px;color:var(--ink)}
.facts{position:absolute;left:16px;top:204px;text-align:left;font-size:11px;line-height:18px;font-weight:300}
.facts dt{float:left;width:32px;font-weight:500}
.experience{left:6px;top:362px;width:188px;height:63px;padding:15px 16px}
.heading{color:var(--green);font-weight:500;font-size:13px}
.experience p{font-size:11px;font-weight:500;margin-top:1px}
.education{left:6px;top:433px;width:188px;height:164px;padding:14px 16px}
.edu-item{margin-top:12px;font-size:10.5px;line-height:16.5px;font-weight:300}
.edu-item strong{font-weight:500;display:block}
.edu-item+.edu-item{margin-top:9px}
.topbar{left:200px;top:0;width:1000px;height:44px;background:var(--topbar)}
.nav{left:25px;top:13px;font-size:11px;font-weight:500;color:var(--slate)}
.nav a{color:inherit;text-decoration:none;margin-right:17px}
.bell{left:860px;top:14px}
.me{left:896px;top:5px;display:flex;align-items:center}
.me .pic{width:35px;height:35px;border-radius:50%;border:1px solid var(--green);padding:2px;background:#fff}
.me .pic span{display:block;width:100%;height:100%;border-radius:50%;background:radial-gradient(circle at 50% 40%,#b89b86,#5c463a 65%)}
.me .who{margin-left:7px;font-size:10px;line-height:11px;color:var(--green)}
.main{left:200px;top:44px;width:800px;height:587px;background:#fff}
.lang-label{left:25px;top:27px;font-size:13px;font-weight:500;color:var(--green)}
.lang{top:25px;width:156px;font-size:9.5px}
.lang .row{display:flex;justify-content:space-between;padding:0 2px}
.lang .bar{margin-top:2px;height:6px;border:1px solid #ddd;border-radius:3px;padding:1px}
.lang .bar i{display:block;height:100%;background:var(--green);border-radius:2px}
.about-h{left:25px;top:62px}
.about{left:25px;top:82px;width:735px;font-size:10.4px;line-height:16.2px;font-weight:300;color:var(--ink)}
.posts-h{left:25px;top:157px}
.post{left:25px;width:737px;height:135px;padding:17px 19px}
.post h3{font-size:11.3px;font-weight:500;color:var(--slate)}
.post p{margin-top:4px;font-size:10.4px;line-height:16.2px;font-weight:300;color:var(--muted)}
.btn{display:inline-block;margin-top:9px;width:78px;height:25px;line-height:25px;text-align:center;border-radius:3px;font-size:9px;font-weight:500;color:#fff;background:var(--slate)}
.btn.active{background:var(--green)}
.track{left:771px;top:183px;width:1px;height:404px;background:#e1e1e1}
.thumb{left:766px;top:317px;width:11px;height:11px;border-radius:50%;background:var(--green);border:2px solid #fff;box-shadow:0 0 0 1px #e1e1e1}
.aside{left:1000px;top:44px;width:200px;height:587px;background:var(--side)}
.history{left:1006px;top:50px;width:188px;height:288px;padding:16px}
.stint{margin-top:9px}
.stint+.stint{margin-top:13px}
.year{display:inline-block;background:var(--green);color:#fff;font-size:8px;padding:1px 6px;border-radius:2px}
.stint h4{margin-top:5px;font-size:10.6px;font-weight:500;line-height:15px}
.stint p{margin-top:3px;font-size:10.2px;line-height:16px;font-weight:300;color:var(--muted)}
.skills{left:1006px;top:344px;width:188px;height:211px;padding:15px 17px}
.skill{margin-top:11px}
.skill+.skill{margin-top:12px}
.skill span{font-size:10.6px;font-weight:500;display:block}
.skill .bar{margin-top:5px;height:6px;background:var(--track);border-radius:3px;padding:1px 1px 1px 1px}
.skill .bar i{display:block;height:100%;background:var(--green);border-radius:2px}
.download{left:1006px;top:561px;width:188px;height:64px;background:var(--green);border-radius:4px;display:flex;align-items:center;padding-left:36px;color:#fff;text-decoration:none}
.download strong{margin-left:9px;font-size:16px;line-height:16.5px;font-weight:600}
.footer{left:0;top:631px;width:1200px;height:31px;background:var(--footer);color:#fff;font-size:10.5px;text-align:center;line-height:31px;font-weight:300}
</style>
</head>
<body>

<aside class="abs sidebar">
  <div class="abs brand"><span class="brand-dot"></span>CVSPIRE</div>

  <section class="abs card profile">
    <div class="avatar"><span role="img" aria-label="Profile photo of the candidate"></span></div>
    <div class="name">Darren <b>Holloway</b></div>
    <div class="role">UI &amp; UX Designer</div>
    <dl class="facts">
      <dt>Age:</dt><dd>38 Years</dd>
      <dt>Sex:</dt><dd>male</dd>
    </dl>
  </section>

  <section class="abs card experience">
    <div class="heading">Work Experience</div>
    <p>15 Years</p>
  </section>

  <section class="abs card education">
    <div class="heading">Education:</div>
    <div class="edu-item"><strong>Enter your major</strong>Name Of Your University<br>2005-2009</div>
    <div class="edu-item"><strong>Enter your major</strong>Name Of Your University<br>2005-2009</div>
  </section>
</aside>

<header class="abs topbar">
  <nav class="abs nav"><a href="#">Jobs</a><a href="#">CV</a></nav>
  <svg class="abs bell" width="16" height="16" viewBox="0 0 16 16" aria-label="Notifications">
    <path d="M7 2.2a4 4 0 0 0-4 4V10L1.8 12h10.4L11 10V6.2a4 4 0 0 0-4-4z" fill="#6a6e71"/>
    <path d="M5.5 13a1.5 1.5 0 0 0 3 0z" fill="#6a6e71"/>
    <circle cx="12.5" cy="2.5" r="2" fill="#84bd32"/>
  </svg>
  <div class="abs me">
    <div class="pic"><span role="img" aria-label="Account avatar photo"></span></div>
    <div class="who">Darren<br>Holloway</div>
  </div>
</header>

<main class="abs main">
  <div class="abs lang-label">Language:</div>
  <div class="abs lang" style="left:108px"><div class="row"><span>Roman</span><span>65%</span></div><div class="bar"><i style="width:57%"></i></div></div>
  <div class="abs lang" style="left:290px"><div class="row"><span>Magyar</span><span>25%</span></div><div class="bar"><i style="width:25%"></i></div></div>
  <div class="abs lang" style="left:472px"><div class="row"><span>English</span><span>100%</span></div><div class="bar"><i style="width:100%"></i></div></div>

  <h2 class="abs heading about-h">About Me:</h2>
  <p class="abs about">Lorem Ipsum is simply dummy text of the printing and typesetting industry. Lorem Ipsum has been the industry's standard dummy text ever since the 1500s, when an unknown printer took a galley of type and scrambled it to make a type specimen book. It has survived not only five centuries, but also the leap into electronic typesetting, remaining essentially unchanged.</p>

  <h2 class="abs heading posts-h">Job Posts:</h2>

  <article class="abs card post" style="top:182px">
    <h3>Job position here</h3>
    <p>Lorem Ipsum is simply dummy text of the printing and typesetting industry. Lorem Ipsum has been the industry's standard dummy text ever since the 1500s, when an unknown printer took a galley of type and scrambled it to make a type specimen book. It has survived not only five centuries, but also the leap into electronic typesetting, remaining essentially unchanged.</p>
    <a class="btn">Apply Now</a>
  </article>
  <article class="abs card post" style="top:325px">
    <h3>Job position here</h3>
    <p>Lorem Ipsum is simply dummy text of the printing and typesetting industry. Lorem Ipsum has been the industry's standard dummy text ever since the 1500s, when an unknown printer took a galley of type and scrambled it to make a type specimen book. It has survived not only five centuries, but also the leap into electronic typesetting, remaining essentially unchanged.</p>
    <a class="btn active">Apply Now</a>
  </article>
  <article class="abs card post" style="top:467px">
    <h3>Job position here</h3>
    <p>Lorem Ipsum is simply dummy text of the printing and typesetting industry. Lorem Ipsum has been the industry's standard dummy text ever since the 1500s, when an unknown printer took a galley of type and scrambled it to make a type specimen book. It has survived not only five centuries, but also the leap into electronic typesetting, remaining essentially unchanged.</p>
    <a class="btn">Apply Now</a>
  </article>

  <div class="abs track"></div>
  <div class="abs thumb"></div>
</main>

<aside class="abs aside"></aside>

<section class="abs card history">
  <div class="heading">Work Experience:</div>
  <div class="stint">
    <span class="year">2012-2014</span>
    <h4>Job position here<br>Company Name/ California</h4>
    <p>Lorem Ipsum is simply dummy text of the printing &amp; typesetting industry.</p>
  </div>
  <div class="stint">
    <span class="year">2012-2014</span>
    <h4>Job position here<br>Company Name/ California</h4>
    <p>Lorem Ipsum is simply dummy text of the printing &amp; typesetting industry.</p>
  </div>
</section>

<section class="abs card skills">
  <div class="heading">Skills:</div>
  <div class="skill"><span>PixelForge</span><div class="bar"><i style="width:85%"></i></div></div>
  <div class="skill"><span>VectorLine</span><div class="bar"><i style="width:53%"></i></div></div>
  <div class="skill"><span>Frameboard</span><div class="bar"><i style="width:93%"></i></div></div>
  <div class="skill"><span>ProtoKit</span><div class="bar"><i style="width:28%"></i></div></div>
</section>

<a class="abs download" href="#">
  <svg width="32" height="32" viewBox="0 0 32 32" aria-hidden="true">
    <rect x="7" y="2" width="18" height="24" rx="2" fill="none" stroke="#fff" stroke-width="2"/>
    <rect x="2" y="8" width="20" height="11" rx="1.5" fill="#fff"/>
    <text x="12" y="16.5" text-anchor="middle" font-family="Poppins,sans-serif" font-size="7" font-weight="600" fill="#84bd32">PDF</text>
    <path d="M26 20v8m-3-3 3 3 3-3" stroke="#fff" stroke-width="2" fill="none"/>
  </svg>
  <strong>Download<br>Resume</strong>
</a>

<footer class="abs footer">Copyright © 2024 CV Spire, All rights reserved</footer>

</body>
</html>
```